Rock, Paper Scissors Championship Flyer

We need a dynamic, bold and exciting flyer to promote the following event at our sports center. The event will be primarily focused for adults, but children are welcome to join

Rock, Paper, Scissors Championship - $$$ prizes
Date: June 9th, 2018
Time: 11am-4pm
Fee: $2 to enter, free for spectators
Heats to determine the overall ‘Rock, Paper, Scissors’ champion!
- Cash prizes on offer
- Live music.
- Food and beverage available for purchase

Belmoray Sports Center, Roselle NJ
908-555-0163
www.belmoraypark.example

Must include our logo (does not have to be huge) and County seal (both attached)

Colors

Designer to choose colors to be used in the design.

Requirements
Must have
• Should be fun and colorful
• The following info and attached logos:
• Rock, Paper, Scissors Championship - $$$ prizes
• Date: June 9th, 2018
• Time: 11am-4pm
• Fee: $2 to enter, free for spectators
• Heats to determine the overall ‘Rock, Paper, Scissors’ champion!
• - Cash prizes on offer
• - Live music.
• - Food and beverage available for purchase
• Belmoray Sports Center, Roselle NJ
• 908-555-0163
• www.belmoraypark.example
Nice to have
• There are a few inspirational photos attached to give an idea of what we are looking for.

```html
<!DOCTYPE html>
<html lang="en">
<head>
<meta charset="utf-8">
<title>Rock, Paper, Scissors Championship</title>
<link rel="stylesheet" href="https://fonts.googleapis.com/css2?family=Alfa+Slab+One&display=swap">
<style>
  :root {
    --band-red: #e3283a;
    --ink: #1c1a1a;
    --navy: #2b4a72;
    --olive: #857430;
    --footer: #e2e6eb;
    --seal-gold: #d9b45a;
    --seal-cream: #f6ecd0;
  }
  * { margin: 0; padding: 0; box-sizing: border-box; }
  html, body { width: 927px; height: 1200px; overflow: hidden; background: #fff; }
  .flyer {
    position: relative;
    width: 927px;
    height: 1200px;
    overflow: hidden;
    font-family: "Alfa Slab One", Georgia, serif;
    font-weight: 400;
  }
  .title-band {
    position: absolute; left: 0; top: 0; width: 927px; height: 125px;
    background: var(--band-red);
  }
  .event-title {
    position: absolute; left: 32px; top: 2px;
    font-size: 45px; line-height: 52px; color: var(--ink); white-space: nowrap; font-weight: 400;
  }
  .event-subtitle {
    position: absolute; left: 109px; top: 50px;
    font-size: 34px; line-height: 36px; color: var(--navy); white-space: nowrap;
  }
  .event-subtitle span { display: block; }
  .event-subtitle .second-line { padding-left: 113px; }

  .hero-photo {
    position: absolute; left: 0; top: 125px; width: 927px; height: 524px;
    background:
      radial-gradient(ellipse at 60% 40%, rgba(230,60,140,.55), transparent 60%),
      linear-gradient(120deg, #b51e2c 0%, #d43a5c 35%, #7a2c8c 60%, #e03a4a 85%, #c42030 100%);
  }
  .county-seal {
    position: absolute; left: 23px; top: 177px; width: 140px; height: 140px;
  }
  .prize-callout {
    position: absolute; left: 0; top: 125px; width: 927px; height: 524px;
  }
  .prize-callout text {
    font-family: "Alfa Slab One", Georgia, serif;
    font-size: 95px;
    fill: #000;
  }

  .summer-scene {
    position: absolute; left: 0; top: 649px; width: 927px; height: 426px;
    background:
      radial-gradient(circle at 50% 70%, rgba(240,170,90,.45) 0 22%, rgba(170,200,150,.35) 23% 32%, transparent 33%),
      linear-gradient(180deg, #eef5f8 0%, #e4eff2 60%, #dfeaec 100%);
  }
  .event-when {
    position: absolute; left: 30px; top: 676px;
    font-size: 31px; line-height: 34px; color: var(--ink); text-align: center; width: 282px;
  }
  .event-fee {
    position: absolute; left: 32px; top: 752px;
    font-size: 25px; color: var(--olive); white-space: nowrap;
  }
  .feature {
    position: absolute; right: 9px;
    font-size: 48px; line-height: 56px; color: var(--navy); white-space: nowrap;
  }
  .feature-cash { top: 650px; }
  .feature-music { top: 968px; }
  .feature-food {
    position: absolute; right: 5px; top: 1028px;
    font-size: 33px; line-height: 40px; color: var(--ink); white-space: nowrap;
  }

  .venue-footer {
    position: absolute; left: 0; top: 1075px; width: 927px; height: 125px;
    background: var(--footer);
  }
  .venue-mark {
    position: absolute; left: 18px; top: 1122px; width: 190px;
    display: flex; align-items: center; gap: 8px;
    font-size: 17px; line-height: 20px; color: #2f3f50;
  }
  .venue-mark .mark-square { width: 22px; height: 22px; background: #2f3f50; flex: none; }
  .venue-name {
    position: absolute; left: 218px; top: 1086px;
    font-size: 35px; line-height: 42px; color: var(--olive); white-space: nowrap;
  }
  .venue-phone {
    position: absolute; left: 222px; top: 1138px;
    font-size: 33px; line-height: 40px; color: var(--olive); white-space: nowrap;
  }
  .venue-web {
    position: absolute; left: 484px; top: 1143px;
    font-size: 26px; line-height: 34px; color: var(--olive); white-space: nowrap;
  }
</style>
</head>
<body>
<main class="flyer">
  <header class="title-band"></header>
  <h1 class="event-title">Rock, Paper, Scissors Championship</h1>
  <p class="event-subtitle">
    <span>Heats to determine the overall</span>
    <span class="second-line">‘Rock, Paper, Scissors’ champion!</span>
  </p>

  <div class="hero-photo" role="img" aria-label="Photo of a cheer team performing on a competition stage with red star shapes"></div>

  <svg class="county-seal" viewBox="0 0 140 140" role="img" aria-label="County seal">
    <circle cx="70" cy="70" r="68" fill="var(--seal-gold)"/>
    <circle cx="70" cy="70" r="52" fill="var(--seal-cream)"/>
  </svg>

  <svg class="prize-callout" viewBox="0 0 927 524" aria-label="$$$ prizes">
    <text x="455" y="300" text-anchor="middle" textLength="940" lengthAdjust="spacingAndGlyphs"
          transform="rotate(-27 455 268)">$$$ prizes</text>
  </svg>

  <div class="summer-scene" role="img" aria-label="Illustration of a boy floating on a swim ring among palm trees"></div>

  <p class="event-when">June 9th, 2018<br>11am-4pm</p>
  <p class="event-fee">$2 to enter, free for spectators</p>

  <p class="feature feature-cash">Cash prizes on offer</p>
  <p class="feature feature-music">Live music</p>
  <p class="feature-food">Food and beverage available for purchase</p>

  <footer class="venue-footer"></footer>
  <div class="venue-mark"><span class="mark-square"></span><span>Belmoray Sports Center</span></div>
  <p class="venue-name">Belmoray Sports Center, Roselle NJ</p>
  <p class="venue-phone">908-555-0163</p>
  <p class="venue-web">www.belmoraypark.example</p>
</main>
</body>
</html>
```